Kitchen Tools Infographic - Helpful Items for Healthy Home Meals

We are a weight loss company that provides holistic, natural nutrition programs to consumers -- you can see our web site at www.FernaluVita.com. We need a simple infographic to be shared on social media and via email. The topic for the infographic is "Equip Your Kitchen for Healthy Home Meals". We've outlined 5 groups of kitchen tools that are helpful for consumers to have for preparing home meals, and included some framing statistics emphasizing the weight management benefits of preparing meals versus eating out.

Target Market(s)

Women age 35-55

Industry/Entity Type

Health And Wellness

Font styles to use
Sans Serif

Colors
0292cd
9bcb3b

Requirements
Must have
• - FernaluVita Logo
• - Graphics summarizing statistic (weight gain)
• - Graphics showing groupings of kitchen tools
Should not have
• body scale graphics
• before/after graphics

```html
<!DOCTYPE html>
<html lang="en">
<head>
<meta charset="utf-8">
<title>Equip Your Kitchen for Healthy Home Meals – FernaluVita</title>
<link rel="stylesheet" href="https://fonts.googleapis.com/css2?family=Arimo:wght@400;700&family=Bebas+Neue&family=Roboto+Condensed:wght@700&display=swap">
<style>
  :root {
    --page-bg: #000000;
    --paper: #ffffff;
    --brand-blue: #1fb5e9;
    --chart-blue: #1f5fa8;
    --chart-red: #e0202a;
    --brand-green: #9bcb3b;
    --ink: #1d1d1d;
    --grid: #cfcfcf;
    --frame: #3a3a3a;
  }
  * { box-sizing: border-box; margin: 0; padding: 0; }
  html, body { width: 1200px; height: 1008px; overflow: hidden; background: var(--page-bg); }
  .flyer {
    position: absolute; left: 276px; top: 20px;
    width: 639px; height: 957px;
    transform: scale(1.0144); transform-origin: 0 0;
    background: var(--paper);
    font-family: "Arimo", Arial, sans-serif; color: var(--ink);
  }
  .hero-photo {
    position: absolute; left: 0; top: 0; width: 639px; height: 177px;
    background:
      radial-gradient(ellipse 140px 70px at 470px 120px, #5aa83a 0%, rgba(90,168,58,0) 100%),
      radial-gradient(ellipse 120px 50px at 150px 150px, #e6c34a 0%, rgba(230,195,74,0) 100%),
      radial-gradient(ellipse 150px 110px at 560px 60px, #e7c9b4 0%, rgba(231,201,180,0) 100%),
      linear-gradient(180deg, #7fb2d8 0%, #bcd6e8 55%, #e9eef0 100%);
  }
  .hero-title {
    position: absolute; left: 36px;
    font-family: "Bebas Neue", "Arial Narrow", sans-serif;
    color: var(--brand-blue);
    -webkit-text-stroke: 5px #ffffff; paint-order: stroke fill;
    line-height: 1; white-space: nowrap;
    transform-origin: 0 0;
  }
  .hero-title--top { top: 47px; font-size: 74px; transform: scaleX(0.93); }
  .hero-title--bottom { top: 113px; font-size: 60px; transform: scaleX(0.87); }

  .intro { position: absolute; left: 36px; top: 196px; width: 590px; }
  .intro-heading { font-size: 17px; font-weight: 700; margin-bottom: 5px; }
  .intro-text { font-size: 14.4px; line-height: 23px; }

  .chart {
    position: absolute; top: 306px; height: 141px;
    border: 1px solid var(--frame); background: var(--paper);
  }
  .chart--calories { left: 19px; width: 292px; }
  .chart--pounds { left: 329px; width: 296px; }
  .chart-title {
    height: 27px; background: var(--brand-blue); color: #fff;
    font-family: "Roboto Condensed", "Arial Narrow", sans-serif; font-weight: 700;
    font-size: 16.5px; line-height: 27px; text-align: center; white-space: nowrap;
  }
  .chart svg { display: block; }
  .chart text { font-family: "Arimo", Arial, sans-serif; font-size: 6px; fill: #333; }

  .tools-panel {
    position: absolute; left: 0; top: 458px; width: 639px; height: 340px;
    background: var(--brand-green);
  }
  .tools-heading {
    position: absolute; left: 0; top: 4px; width: 100%; text-align: center;
    color: #fff; font-weight: 700; font-size: 19px;
  }
  .tool-group {
    position: absolute; left: 26px; width: 586px; height: 55px;
    background: var(--paper); font-size: 12.6px; line-height: 15.5px;
    padding-top: 4px;
  }
  .tool-number { position: absolute; left: 7px; top: 4px; }
  .tool-list { position: absolute; left: 45px; top: 4px; list-style: none; white-space: nowrap; }
  .tool-list b { font-weight: 700; }

  .closing {
    position: absolute; left: 0; top: 806px; width: 639px; text-align: center;
    font-size: 18.5px; line-height: 23px;
  }
  .brand-name {
    position: absolute; left: 0; top: 857px; width: 639px; text-align: center;
    font-family: "Arimo", Arial, sans-serif; font-weight: 700;
    font-size: 50px; letter-spacing: -1.5px; color: var(--brand-blue); line-height: 1;
  }
  .site-band {
    position: absolute; left: 0; top: 921px; width: 639px; height: 36px;
    background: var(--brand-blue); color: #fff; text-align: center;
    font-size: 20px; line-height: 36px; letter-spacing: 5px;
  }
</style>
</head>
<body>
<main class="flyer">
  <div class="hero-photo" role="img" aria-label="Photo of hands slicing green pepper on a cutting board with cherry tomatoes and yellow peppers"></div>
  <h1>
    <span class="hero-title hero-title--top">EQUIP YOUR</span>
    <span class="hero-title hero-title--bottom">KITCHEN FOR HEALTHY HOMEMEALS</span>
  </h1>

  <section class="intro">
    <h2 class="intro-heading">Why Cook at Home?</h2>
    <p class="intro-text">Those who eat out consume an average of 134 calories more per meal.&nbsp; Americans eat out an average of 4.5 times per week, so those extra calories can add up to substantial weight gain -- and give you a reason to prepare your own meals.</p>
  </section>

  <figure class="chart chart--calories">
    <figcaption class="chart-title">Excess Calories from Restaurant Meals</figcaption>
    <svg width="290" height="112" viewBox="0 0 290 112">
      <g stroke="var(--grid)" stroke-width="1">
        <line x1="67" y1="10" x2="67" y2="90"/><line x1="96" y1="10" x2="96" y2="90"/>
        <line x1="125" y1="10" x2="125" y2="90"/><line x1="154" y1="10" x2="154" y2="90"/>
        <line x1="183" y1="10" x2="183" y2="90"/><line x1="212" y1="10" x2="212" y2="90"/>
        <line x1="241" y1="10" x2="241" y2="90"/><line x1="270" y1="10" x2="270" y2="90"/>
      </g>
      <rect x="67" y="58" width="175" height="4" fill="var(--chart-blue)"/>
      <rect x="67" y="76" width="39" height="4" fill="var(--chart-blue)"/>
      <text x="7" y="62">Calories Per Week</text>
      <text x="9" y="80">Calories Per Meal</text>
      <g text-anchor="middle">
        <text x="67" y="100">0</text><text x="96" y="100">100</text><text x="125" y="100">200</text>
        <text x="154" y="100">300</text><text x="183" y="100">400</text><text x="212" y="100">500</text>
        <text x="241" y="100">600</text><text x="270" y="100">700</text>
      </g>
    </svg>
  </figure>

  <figure class="chart chart--pounds">
    <figcaption class="chart-title">Pounds Gained from Restaurant Meals</figcaption>
    <svg width="294" height="112" viewBox="0 0 294 112">
      <g stroke="var(--grid)" stroke-width="1">
        <line x1="24" y1="16" x2="284" y2="16"/><line x1="24" y1="30" x2="284" y2="30"/>
        <line x1="24" y1="44" x2="284" y2="44"/><line x1="24" y1="57" x2="284" y2="57"/>
        <line x1="24" y1="71" x2="284" y2="71"/><line x1="24" y1="84" x2="284" y2="84"/>
      </g>
      <g text-anchor="end">
        <text x="14" y="18">10</text><text x="14" y="32">8</text><text x="14" y="46">6</text>
        <text x="14" y="59">4</text><text x="14" y="73">2</text><text x="14" y="86">0</text>
      </g>
      <rect x="49" y="75" width="11" height="9" fill="var(--chart-red)"/>
      <rect x="114" y="54" width="11" height="30" fill="var(--chart-red)"/>
      <rect x="180" y="23" width="11" height="61" fill="var(--chart-red)"/>
      <g text-anchor="middle">
        <text x="55" y="99">2 months</text><text x="120" y="99">6 months</text><text x="185" y="99">1 year</text>
      </g>
    </svg>
  </figure>

  <section class="tools-panel">
    <h2 class="tools-heading">Make healthy eating easier with these kitchen tools:</h2>

    <div class="tool-group" style="top:32px">
      <span class="tool-number">1)</span>
      <ul class="tool-list">
        <li><b>PREP:</b>&nbsp; Cutting Board–essential for prepping meat and vegetables</li>
        <li>Chef's Knife–go for quality to make chopping, dicing and slicing faster and easier</li>
        <li>Digital Food Scale– get the precision you need for perfect recipes and portion control</li>
      </ul>
    </div>

    <div class="tool-group" style="top:93px">
      <span class="tool-number">2)</span>
      <ul class="tool-list">
        <li><b>TECH:</b> High-Powered Blender–make highly nutritious, healthy drinks from fruits and veggies</li>
        <li>Slow Cooker- cook delicious meals while you are at work</li>
        <li>Pressure Cooker-create single pot meals in 20 minutes or less</li>
      </ul>
    </div>

    <div class="tool-group" style="top:152px">
      <span class="tool-number">3)</span>
      <ul class="tool-list">
        <li><b>COOK:</b> Ceramic Pan–nonstick cooking surface allows you to cook without oil</li>
        <li>Vegetable Steamer– preserve nutrients and natural, fresh taste</li>
        <li>Baking Sheet–ideal for roasting vegetables in the oven or baking chicken and fish dishes</li>
      </ul>
    </div>

    <div class="tool-group" style="top:213px">
      <span class="tool-number">4)</span>
      <ul class="tool-list">
        <li><b>SERVE:</b> Cloth Napkins – to reduce waste and dress up your table</li>
        <li>Dinnerware–pre-plate meals rather than serving family style to control portions</li>
        <li>Small Plates – use salad plates and smaller dishware to manage perception of food volume</li>
      </ul>
    </div>

    <div class="tool-group" style="top:273px">
      <span class="tool-number">5)</span>
      <ul class="tool-list">
        <li><b>STORE:</b> Glass Storage Containers–keep your healthy leftovers so nothing goes to waste</li>
        <li>Mason Jars – perfect for premade salads that you can bring to work</li>
        <li>Freezer Safe Re-Sealable Bags –prepare double batches to make the most of your time</li>
      </ul>
    </div>
  </section>

  <p class="closing">FernaluVita can help you develop healthier eating habits.<br>We invite you to learn more.</p>
  <div class="brand-name">FERNALUVITA</div>
  <div class="site-band">www.FernaluVita.com</div>
</main>
</body>
</html>
```